Web design for boutique law firm

Web design for law firm; practice areas include:
-international intellectual property counseling
-general corporate (contract negotiation, licensing, distribution agreements
-see my *very* outdated website at www.pvtlegalhouse.com: here is some of the home page content:

"PVT Law Group enjoys providing proactive, business-minded, efficient legal solutions for individuals and companies that benefit from major law firm experience at reasonable rates.

Some areas of emphasis include:

Counseling individuals and companies with respect to clearing, selecting, securing, managing, commercializing, and protecting intellectual property assets around the world. This includes traditional global brand management, marketing, advertising, and enforcement work as well as litigation.
PVT Law Group also provides general counseling services for individuals and businesses, from start-up advice to sophisticated business transactions strategy, agreement negotiating, dispute resolution, and litigation.
Before founding PVT Law Group in 2008, Curtis L. Abernathy led the Trademark, Copyright, & Brand Management Group for Falkner & Ingleby's Seattle office. Curtis was also a senior associate at Silicon Valley based Hartwell, Bexley, Oduya, & Penrose."

Target Market(s)

Clients/potential clients needing tier one, international intellectual property advice with "mega" law firm experience for much less than what we were/would be charging at the "mega firms".

Industry/Entity Type

Legal

Number of Pages Required

4 page

Font styles to use
Serif
Sans Serif

Colors

Designer to choose colors to be used in the design.

Requirements
Must have
• +Improvement over everything on current site at www.pvtlegalhouse.com.
• +Pictures/bios for me and my team (four of us right now).
• +Easy to update and add/remove content.
• +Must be superior in design (look, feel, ease of use, classy and elegant, but hip, reflects international practice).
• +i have logos and color schemes (see current website) but will consider improvements.
Nice to have
• Let me know your thoughts.
Should not have
• No cheese; no overt sales pitches or marketing (since law firm).

```html
<!DOCTYPE html>
<html lang="en">
<head>
<meta charset="utf-8">
<title>PVT Law Group PLLC</title>
<link rel="stylesheet" href="https://fonts.googleapis.com/css2?family=Cinzel:wght@400&family=Lora:wght@400;700&family=Montserrat:wght@500&family=Raleway:wght@400;500;600&display=swap">
<style>
:root{
  --orange:#f47a20;
  --orange-dark:#e0651a;
  --ink:#222;
  --text:#333;
  --muted:#555;
  --navy:#1d3a5c;
  --dark:#2e2e2e;
  --darker:#1f1f1f;
  --grey-bg:#ebebeb;
  --line:#cfcfcf;
  --white:#fff;
}
*{box-sizing:border-box;margin:0;padding:0}
html,body{width:1200px;height:2546px;overflow:hidden;background:var(--white)}
body{position:relative;font-family:"Raleway",Arial,sans-serif;color:var(--text)}
.abs{position:absolute}
.serif{font-family:"Lora",Georgia,serif}

/* top bar */
.topbar{left:0;top:0;width:1200px;height:36px;background:var(--orange);color:var(--white);font-size:14px}
.topbar .follow{left:170px;top:9px}
.social{top:6px;width:24px;height:24px;border-radius:50%;background:var(--ink)}
.topbar .mail{left:692px;top:12px;width:18px;height:12px}
.topbar .email{left:716px;top:9px}
.topbar .phone-ico{left:893px;top:9px}
.topbar .phone{left:920px;top:6px;font-size:20px}

/* header */
.header{left:0;top:36px;width:1200px;height:81px;background:var(--white)}
.brand{left:166px;top:22px;font-family:"Raleway",sans-serif;font-weight:500;font-size:26px;color:var(--orange);letter-spacing:.5px;white-space:nowrap}
.nav{right:161px;top:42px;display:flex;font-family:"Lora",serif;font-size:14px;color:var(--ink)}
.nav span{padding:0 13px;border-left:1px solid var(--line);line-height:16px}
.nav span:first-child{border-left:0}
.nav .active{color:var(--orange);font-weight:700}

/* hero */
.hero{left:0;top:117px;width:1200px;height:413px;background:linear-gradient(180deg,#2b3340 0%,#6c7a88 40%,#3c4654 75%,#1d2430 100%)}
.hero-caption{left:0;top:345px;width:1200px;text-align:center;color:var(--white);font-family:"Montserrat",sans-serif;font-weight:500;font-size:24px;line-height:30px}
.slide-arrow{top:180px;width:34px;height:28px;background:rgba(0,0,0,.55);border:1px solid rgba(255,255,255,.5)}

/* welcome */
.portrait{left:161px;top:567px;width:209px;height:225px;border:1px solid var(--line);padding:5px;background:var(--white)}
.portrait div{width:100%;height:100%;background:linear-gradient(180deg,#cfcfcf,#7a7a7a 70%,#2c2c2c)}
.welcome-title{left:394px;top:596px;font-family:"Lora",serif;font-size:29px;color:var(--orange)}
.welcome-text{left:394px;top:652px;width:640px;font-size:11.5px;line-height:20px;color:var(--ink)}
.btn{background:var(--orange);color:var(--white);font-family:"Lora",serif;text-align:center}
.read-more{left:394px;top:750px;width:127px;height:32px;line-height:32px;font-size:14px}

/* services */
.services{left:0;top:828px;width:1200px;height:742px;background:linear-gradient(180deg,#0f1c2d 0%,#1f3043 45%,#3a4753 75%,#2a3340 100%)}

/* cta */
.cta-title{left:0;top:1597px;width:1200px;text-align:center;font-family:"Lora",serif;font-size:27px;color:var(--ink)}
.cta-btn{left:526px;top:1653px;width:122px;height:32px;line-height:32px;font-size:15px}

/* inquiry + reviews */
.band{left:0;top:1726px;width:1200px;height:322px;background:var(--grey-bg)}
.sec-title{font-family:"Lora",serif;font-size:22px;color:var(--ink)}
.sec-title em{font-style:normal;color:var(--orange)}
.rule{height:2px;width:34px;background:var(--ink)}
.field{background:var(--white);border:1px solid var(--line);font-size:11px;color:var(--muted);padding:7px 8px}
.submit{font-family:"Lora",serif;font-size:13px;background:var(--orange);color:var(--white);text-align:center;letter-spacing:.5px}
.divider{left:599px;top:1770px;width:1px;height:240px;background:var(--line)}
.quote{left:631px;top:1814px;width:408px;height:158px;border:1px solid #999;border-radius:8px;background:var(--white);padding:16px 20px 0 44px;font-style:italic;font-size:12px;line-height:19px;color:var(--ink)}
.quote-mark{left:645px;top:1808px;font-family:"Lora",serif;font-size:44px;color:#bbb}
.reviewer{left:780px;top:1984px;width:200px;text-align:center;font-family:"Lora",serif;font-size:12px;color:var(--ink)}

/* consultation */
.consult-title{left:163px;top:2090px;font-family:"Cinzel",serif;font-size:24px;color:var(--ink)}
.consult-title span{color:var(--navy)}
.consult-text{left:163px;top:2150px;width:470px;font-size:11.5px;line-height:20px;color:var(--ink)}
.contact-line{font-size:11.5px;color:var(--ink);line-height:18px}
.dot-ico{width:17px;height:17px;border-radius:50%;background:var(--orange)}

/* footer */
.footer{left:0;top:2376px;width:1200px;height:170px}
.footer-brand{left:166px;top:2430px;font-family:"Raleway",sans-serif;font-weight:500;font-size:21px;color:#9a9a9a;white-space:nowrap}
.footer-nav{left:150px;top:2474px;display:flex;font-family:"Lora",serif;font-size:13px;color:#ddd}
.footer-nav span{padding:0 13px;border-left:1px solid #666;line-height:15px}
.footer-nav span:first-child{border-left:0}
.footer-nav .active{color:var(--orange)}
.legal{left:825px;top:2477px;display:flex;font-size:11.5px;color:#ddd}
.legal span{padding:0 12px;border-left:1px solid #666;line-height:14px}
.legal span:first-child{border-left:0}
.copy{left:0;top:2508px;width:1200px;height:38px;background:var(--darker);color:#ddd;font-family:"Lora",serif;font-size:11.5px}
</style>
</head>
<body>

<!-- top bar -->
<div class="abs topbar">
  <span class="abs follow">Follow Us On</span>
  <span class="abs social" style="left:271px"></span>
  <span class="abs social" style="left:302px"></span>
  <span class="abs social" style="left:333px"></span>
  <span class="abs social" style="left:364px"></span>
  <svg class="abs mail" viewBox="0 0 18 12"><rect x=".5" y=".5" width="17" height="11" fill="none" stroke="#fff"/><path d="M.5 .5 9 7l8.5-6.5" fill="none" stroke="#fff"/></svg>
  <span class="abs email">info@pvtlegalhouse.com</span>
  <svg class="abs phone-ico" width="20" height="20" viewBox="0 0 20 20"><circle cx="10" cy="10" r="9" fill="none" stroke="#fff" stroke-width="1.5"/><path d="M7 5.5c-1 .8-1 2.5 1 5s4 3.3 5 2.6l.9-1-2-1.5-1 .8c-.8-.3-2-1.6-2.4-2.4l.8-1L8 5z" fill="#fff"/></svg>
  <span class="abs phone">206.555.0148</span>
</div>

<!-- header -->
<header class="abs header">
  <div class="abs brand">PVT LAW GROUP PLLC</div>
  <nav class="abs nav">
    <span class="active">Home</span><span>About Us</span><span>Services</span><span>Our Team</span><span>Our Experience</span><span>Contact Us</span>
  </nav>
</header>

<!-- hero -->
<section class="abs hero" role="img" aria-label="Photo of two business people exchanging documents in front of a city skyline"></section>
<div class="abs hero-caption">We Provide&nbsp; Efficient Legal Solutions For Individuals &amp; Companies That Benefit<br>From Major Law Firm Experience At Reasonable Rates</div>
<svg class="abs slide-arrow" style="left:0;top:297px" viewBox="0 0 34 28"><path d="M20 8l-6 6 6 6" fill="none" stroke="#fff" stroke-width="2"/></svg>
<svg class="abs slide-arrow" style="left:1166px;top:297px" viewBox="0 0 34 28"><path d="M14 8l6 6-6 6" fill="none" stroke="#fff" stroke-width="2"/></svg>

<!-- welcome -->
<div class="abs portrait"><div role="img" aria-label="Portrait photo of the firm's founding attorney"></div></div>
<h1 class="abs welcome-title">Welcome to PVT Law Group PLLC</h1>
<svg class="abs" style="left:540px;top:638px" width="245" height="3"><rect width="245" height="2" fill="#f47a20"/></svg>
<p class="abs welcome-text">PVT Law Group enjoys providing proactive, business-minded, efficient legal solutions for individuals &amp; companies that benefit from major law firm experience at reasonable rates. Some areas of emphasis include:&nbsp; Counseling individuals and companies with respect to clearing, selecting, securing, managing, commercializing, and protecting intellectual property assets around the world.</p>
<div class="abs btn read-more">Read More &#8594;</div>

<!-- services -->
<section class="abs services" role="img" aria-label="Night city skyline photo behind the services diagram">
<svg width="1200" height="742" viewBox="0 0 1200 742" font-family="Raleway, Arial, sans-serif">
  <text x="600" y="68" text-anchor="middle" fill="#fff" font-family="Lora, Georgia, serif" font-size="26">Our Services</text>
  <rect x="584" y="84" width="32" height="2" fill="#fff"/>

  <circle cx="599" cy="394" r="140" fill="none" stroke="#fff" stroke-width="1.5" stroke-dasharray="2 4" opacity=".8"/>
  <text x="599" y="412" text-anchor="middle" fill="#fff" opacity=".35" font-size="52" font-weight="500">PVT</text>

  <g stroke="#fff" stroke-width="2">
    <line x1="652" y1="262" x2="652" y2="298"/>
    <line x1="735" y1="308" x2="704" y2="338"/>
    <line x1="767" y1="411" x2="738" y2="411"/>
    <line x1="712" y1="540" x2="687" y2="515"/>
    <line x1="599" y1="575" x2="599" y2="538"/>
    <line x1="480" y1="545" x2="502" y2="515"/>
    <line x1="432" y1="436" x2="464" y2="436"/>
    <line x1="456" y1="295" x2="522" y2="304"/>
    <line x1="511" y1="262" x2="511" y2="290"/>
  </g>
  <g fill="#fff" stroke="#1a2838" stroke-width="2">
    <circle cx="652" cy="298" r="7"/><circle cx="704" cy="338" r="7"/><circle cx="738" cy="411" r="7"/>
    <circle cx="687" cy="515" r="7"/><circle cx="599" cy="538" r="7"/><circle cx="502" cy="515" r="7"/>
    <circle cx="464" cy="436" r="7"/><circle cx="522" cy="304" r="7"/><circle cx="511" cy="290" r="7"/>
  </g>

  <g fill="#f2f2f2" stroke="#d8d8d8" stroke-width="3">
    <circle cx="652" cy="211" r="49"/><circle cx="765" cy="275" r="49"/><circle cx="815" cy="411" r="49"/>
    <circle cx="748" cy="567" r="49"/><circle cx="599" cy="623" r="49"/><circle cx="445" cy="575" r="49"/>
    <circle cx="384" cy="436" r="49"/><circle cx="411" cy="295" r="49"/><circle cx="511" cy="211" r="49"/>
  </g>

  <g fill="#2a2a2a" stroke="none">
    <!-- 1 person -->
    <circle cx="648" cy="191" r="7"/><path d="M636 228v-22c0-5 4-7 12-7s12 2 12 7v22z"/><rect x="658" y="214" width="12" height="12"/>
    <!-- 2 shield check -->
    <path d="M765 250l22 8v12c0 16-10 26-22 31-12-5-22-15-22-31v-12z"/>
    <path d="M755 275l8 8 14-16" fill="none" stroke="#f2f2f2" stroke-width="4"/>
    <!-- 3 tags -->
    <path d="M793 416l14-22 10 6-14 22z"/><path d="M813 422l14-22 10 6-14 22z"/>
    <!-- 4 gavel -->
    <rect x="732" y="548" width="24" height="12" transform="rotate(-40 744 554)"/><rect x="748" y="560" width="6" height="26" transform="rotate(-40 751 573)"/><rect x="728" y="588" width="26" height="5"/>
    <!-- 5 megaphone -->
    <path d="M582 614h8l20-12v42l-20-12h-8z"/><rect x="615" y="617" width="4" height="12"/>
    <!-- 6 document pen -->
    <rect x="428" y="553" width="28" height="38" fill="none" stroke="#2a2a2a" stroke-width="3"/><rect x="434" y="563" width="16" height="3"/><rect x="434" y="571" width="16" height="3"/><rect x="434" y="579" width="10" height="3"/>
    <!-- 7 head -->
    <path d="M372 462v-10c-8-4-12-12-10-22 3-12 14-18 25-16 11 2 18 11 17 22l4 7h-5v8c0 3-3 5-6 5h-5v6z"/><circle cx="384" cy="428" r="5" fill="#f2f2f2"/>
    <!-- 8 document -->
    <rect x="397" y="275" width="28" height="40" fill="none" stroke="#2a2a2a" stroke-width="3"/><rect x="403" y="285" width="16" height="3"/><rect x="403" y="293" width="16" height="3"/><rect x="403" y="301" width="16" height="3"/>
    <!-- 9 meeting -->
    <circle cx="500" cy="196" r="6"/><circle cx="522" cy="196" r="6"/><path d="M490 216c0-8 4-10 10-10s10 2 10 10z"/><path d="M512 216c0-8 4-10 10-10s10 2 10 10z"/><rect x="486" y="218" width="50" height="5"/><rect x="492" y="223" width="4" height="10"/><rect x="526" y="223" width="4" height="10"/>
  </g>

  <g fill="#fff" stroke="#1a2838" stroke-width="1"><circle cx="692" cy="171" r="15"/><circle cx="810" cy="315" r="15"/><circle cx="770" cy="452" r="15"/><circle cx="788" cy="538" r="15"/><circle cx="641" cy="578" r="15"/><circle cx="491" cy="617" r="15"/><circle cx="429" cy="478" r="15"/><circle cx="371" cy="337" r="15"/><circle cx="480" cy="181" r="15"/></g>
  <g fill="#222" font-size="15" font-weight="600" text-anchor="middle"><text x="692" y="176">1</text><text x="810" y="320">2</text><text x="770" y="457">3</text><text x="788" y="543">4</text><text x="641" y="583">5</text><text x="491" y="622">6</text><text x="429" y="483">7</text><text x="371" y="342">8</text><text x="480" y="186">9</text></g>

  <g fill="#fff" font-size="11">
    <g text-anchor="end">
      <text x="438" y="150" font-size="15">Counseling Individuals</text>
      <text x="438" y="168">Duis autem vel eum iriureo</text><text x="438" y="182">dolor in hendrerit in</text><text x="438" y="196">vulputmi velit consequat</text>
      <text x="333" y="261" font-size="15">Docketing and</text><text x="333" y="278" font-size="15">Paralegal Services</text>
      <text x="333" y="296">Duis autem vel eum iriureo</text><text x="333" y="310">dolor in hendrerit in</text><text x="333" y="324">vulputmi velit consequat</text>
      <text x="319" y="410" font-size="15">IP Counsel and</text><text x="319" y="427" font-size="15">Management</text>
      <text x="319" y="445">Duis autem vel eum iriureo</text><text x="319" y="459">dolor in hendrerit in</text><text x="319" y="473">vulputmi velit consequat</text>
      <text x="377" y="554" font-size="15">Due Diligence</text>
      <text x="377" y="572">Duis autem vel eum iriureo</text><text x="377" y="586">dolor in hendrerit in</text><text x="377" y="600">vulputmi velit consequat</text>
    </g>
    <text x="735" y="152" font-size="15">Brand Management</text>
    <text x="735" y="170">Duis autem vel eum iriureo</text><text x="735" y="184">dolor in hendrerit in vulputmi</text><text x="735" y="198">velit consequat</text>
    <text x="852" y="252" font-size="15">Brand Enforcement</text>
    <text x="852" y="270">Duis autem vel eum iriureo</text><text x="852" y="284">dolor in hendrerit in vulputmi</text><text x="852" y="298">velit consequat</text>
    <text x="882" y="391" font-size="15">Counterfeiting</text>
    <text x="882" y="409">Duis autem vel eum iriureo</text><text x="882" y="423">dolor in hendrerit in vulputmi</text><text x="882" y="437">velit consequat</text>
    <text x="832" y="549" font-size="15">Litigation</text>
    <text x="832" y="567">Duis autem vel eum iriureo</text><text x="832" y="581">dolor in hendrerit in vulputmi</text><text x="832" y="595">velit consequat</text>
    <text x="665" y="651" font-size="15">Rebranding</text>
    <text x="665" y="669">Duis autem vel eum iriureo</text><text x="665" y="683">dolor in hendrerit in vulputmi</text><text x="665" y="697">velit consequat</text>
  </g>
</svg>
</section>

<!-- call to action -->
<h2 class="abs cta-title">Having Any Legal Issues?&nbsp; We Wil Help You</h2>
<div class="abs btn cta-btn">Call Us Today</div>

<!-- inquiry and reviews -->
<section class="abs band"></section>
<svg class="abs" style="left:163px;top:1757px" width="22" height="22" viewBox="0 0 22 22"><rect x="2" y="3" width="15" height="17" fill="none" stroke="#f47a20" stroke-width="2"/><path d="M5 8h9M5 12h9M5 16h6" stroke="#f47a20" stroke-width="1.5"/></svg>
<h3 class="abs sec-title" style="left:191px;top:1753px"><em>Quick</em> Inquiry</h3>
<div class="abs rule" style="left:163px;top:1797px"></div>
<div class="abs field" style="left:163px;top:1822px;width:184px;height:28px">Name</div>
<div class="abs field" style="left:365px;top:1822px;width:184px;height:28px">Email</div>
<div class="abs field" style="left:163px;top:1862px;width:184px;height:28px">Phone</div>
<div class="abs field" style="left:365px;top:1862px;width:184px;height:28px">Select Services</div>
<svg class="abs" style="left:528px;top:1872px" width="10" height="8"><path d="M1 1l4 4 4-4" fill="none" stroke="#2c6ba0" stroke-width="1.5"/></svg>
<div class="abs field" style="left:163px;top:1897px;width:386px;height:65px">Messages</div>
<div class="abs submit" style="left:163px;top:1977px;width:76px;height:27px;line-height:27px">SUBMIT</div>

<div class="abs divider"></div>

<svg class="abs" style="left:631px;top:1758px" width="20" height="18" viewBox="0 0 20 18"><path d="M1 1h12v8H6l-4 3V9H1z" fill="#f47a20"/><path d="M15 5h4v8h-1v3l-3-3H8v-2h7z" fill="#f47a20"/></svg>
<h3 class="abs sec-title" style="left:667px;top:1753px"><em>Happy</em> Customer Reviews</h3>
<div class="abs rule" style="left:631px;top:1797px"></div>
<svg class="abs" style="left:1002px;top:1762px" width="38" height="16"><circle cx="8" cy="8" r="7" fill="none" stroke="#bbb"/><path d="M10 4l-4 4 4 4" fill="none" stroke="#bbb" stroke-width="1.5"/><circle cx="29" cy="8" r="7" fill="none" stroke="#222"/><path d="M27 4l4 4-4 4" fill="none" stroke="#222" stroke-width="1.5"/></svg>
<div class="abs quote">vLorem ipsum dolor sit amet, consectetuer adipiscing elit, sed diam nonummy nibh euismod tincidunt ut laoreet dolore magna aliquam erat volutpat. Ut wisi enim ad minim veniam, quis nostrud exerci tation ullamcorper suscipit lobortis nisl ut aliquip ex ea commodo consequat.</div>
<div class="abs quote-mark">&#8220;</div>
<svg class="abs" style="left:880px;top:1970px" width="40" height="18"><path d="M1 1l18 15L39 1" fill="#fff" stroke="#999"/><rect x="2" y="0" width="36" height="2" fill="#fff"/></svg>
<div class="abs reviewer">Lorem Isumf Lorem</div>

<!-- consultation -->
<h2 class="abs consult-title">Free Consultation? <span>An Appointment?</span></h2>
<p class="abs consult-text">Lorem ipsum dolor sit amet, consectetuer adipiscing elit, sed diam nonummy nibh euismod tincidunt ut laoreet dolore magna aliquam erat volutpat adipiscing elit consectetuer adipisc.</p>
<span class="abs dot-ico" style="left:163px;top:2224px"></span>
<div class="abs contact-line" style="left:192px;top:2222px">PVT Law Group PLLC<br>442 Alder Lane, Suite C, Seattle WA 98107</div>
<span class="abs dot-ico" style="left:163px;top:2280px"></span>
<div class="abs contact-line" style="left:192px;top:2280px">206.555.0148</div>
<span class="abs dot-ico" style="left:310px;top:2278px"></span>
<div class="abs contact-line" style="left:339px;top:2278px">206.555.0149</div>
<span class="abs dot-ico" style="left:163px;top:2322px"></span>
<div class="abs contact-line" style="left:192px;top:2320px">curtis@pvtlegalhouse.com</div>

<div class="abs field" style="left:686px;top:2094px;width:351px;height:31px">Name</div>
<div class="abs field" style="left:686px;top:2138px;width:351px;height:31px">Email</div>
<div class="abs field" style="left:686px;top:2182px;width:351px;height:31px">Phone</div>
<div class="abs field" style="left:686px;top:2226px;width:351px;height:65px">Message</div>
<div class="abs submit" style="left:686px;top:2304px;width:103px;height:34px;line-height:34px;font-size:15px">SUBMIT</div>

<!-- footer -->
<div class="abs footer">
<svg width="1200" height="132" viewBox="0 0 1200 132">
  <path d="M0 60C250 -5 600 10 1200 45V132H0z" fill="#f47a20"/>
  <path d="M0 68C260 8 600 22 1200 55V132H0z" fill="#2e2e2e"/>
</svg>
</div>
<div class="abs footer-brand">PVT LAW GROUP PLLC</div>
<nav class="abs footer-nav"><span class="active">Home</span><span>About Us</span><span>Services</span><span>Our Team</span><span>Our Experience</span><span>Contact Us</span></nav>
<div class="abs legal"><span>Privacy Policy</span><span>Terms &amp; Conditions</span></div>
<div class="abs copy">
  <span class="abs" style="left:165px;top:12px">Copyright &copy; 2017 PVT LAW GROUP, PLLC. All Rights Reserved.</span>
  <svg class="abs" style="left:906px;top:8px" width="24" height="20" viewBox="0 0 24 20"><rect x="2" y="5" width="18" height="12" rx="2" fill="none" stroke="#fff" stroke-width="1.5"/><rect x="2" y="8" width="18" height="2" fill="#fff"/></svg>
  <span class="abs" style="left:935px;top:11px;font-size:13px">Client Payment</span>
</div>

</body>
</html>
```